Präsentationsvorlagen für Vorträge
Zielgruppe
Wir machen laborbasierte Selbsttests im Bereich Longevity und bieten dazu auch passende Supplements an
Aufgabenstellung
Ich brauche eine Präsentationsvorlage für Vorträge basierend auf den Farben und Logo in den angehängten Dateien. Soll alles was für Präsentation nötig ist berücksichtigen

```html
<!DOCTYPE html>
<html lang="de">
<head>
<meta charset="utf-8">
<title>Lumavita – Präsentationsvorlage</title>
<link href="https://fonts.googleapis.com/css2?family=Montserrat:ital,wght@0,400;0,500;0,600;0,700;1,400;1,500&display=swap" rel="stylesheet">
<style>
:root{
  --teal:#0b4a4f;
  --teal-dark:#07464d;
  --green:#8cc63f;
  --panel:#bfd6d6;
  --stage:#efefef;
  --white:#ffffff;
  --card-line:#a9c4ef;
  --muted:#4a5a5c;
  --frame:#cfd6d6;
}
*{margin:0;padding:0;box-sizing:border-box}
html,body{width:1200px;height:2442px;overflow:hidden}
body{font-family:"Montserrat",sans-serif;background:var(--stage);position:relative;color:var(--teal)}
.overview{position:absolute;left:0;top:0;width:1200px;height:740px;background:var(--stage)}
.mini{position:absolute;width:360px;height:197px;overflow:hidden;box-shadow:0 6px 14px rgba(0,0,0,.12)}
.mini .slide{transform:scale(.6383);transform-origin:0 0;position:absolute;left:0;top:0}
.sheet{position:absolute;left:0;top:740px;width:1200px;height:1680px;background:var(--panel)}
.foot{position:absolute;left:0;top:2420px;width:1200px;height:22px;background:var(--stage)}
.slide{position:absolute;width:564px;height:308px;background:var(--white);overflow:hidden}
.slide.dark{background:var(--teal)}
.brand{position:absolute;left:24px;top:14px;display:flex;align-items:center;gap:5px;font-weight:700;font-size:13px;color:var(--teal)}
.brand i{width:10px;height:10px;border-radius:50%;background:var(--green);display:block}
.dark .brand{color:var(--white)}
.h{position:absolute;color:var(--green);font-weight:700;font-size:24px;line-height:1.12;text-align:center}
ul.list{position:absolute;list-style:none;color:var(--teal)}
ul.list li{position:relative;padding-left:16px}
ul.list li::before{content:"•";position:absolute;left:2px}
/* title */
.title-word{position:absolute;left:0;right:0;top:108px;text-align:center;font-size:46px;font-weight:700;color:var(--teal);display:flex;justify-content:center;align-items:center;gap:12px}
.title-word i{width:26px;height:26px;border-radius:50%;background:var(--green);display:block}
.title-tag{position:absolute;left:0;right:0;top:172px;text-align:center;font-size:18px;font-weight:600;color:var(--green)}
/* health */
.photo-couple{position:absolute;right:0;top:0;width:330px;height:308px;background:linear-gradient(90deg,#ffffff 0%,rgba(255,255,255,0) 35%),linear-gradient(160deg,#7ea56a,#c8d9b4 45%,#9ab486 70%,#5f8a5a)}
.health .h{left:40px;width:300px;top:52px}
.health .sub{position:absolute;left:30px;top:118px;font-size:11.5px;font-weight:600;color:var(--green)}
.health ul.list{left:30px;top:170px;font-size:15.5px;font-weight:500;line-height:1.18}
.health ul.list li{margin-bottom:5px}
/* features */
.feat .h{left:195px;width:360px;top:44px}
.pic{position:absolute;width:90px;height:86px;border:4px solid var(--green);border-radius:12px}
.feat ul.list{left:228px;top:104px;width:326px;font-size:13.5px;line-height:1.08}
.feat ul.list li{margin-bottom:4px}
.feat b{font-weight:700}
.feat em{font-style:italic}
/* products */
.prod .h{left:0;right:0;top:32px}
.jar-box{position:absolute;top:96px;width:112px;height:112px;border:1.5px solid var(--frame)}
.jar{position:absolute;left:28px;top:16px;width:56px;height:80px;border-radius:6px;background:linear-gradient(90deg,#c4c9cb,#eef0f0 45%,#b7bdbf)}
.prod-name{position:absolute;top:229px;width:170px;text-align:center;font-size:9px;line-height:1.35}
.prod-name span{display:block;color:var(--green);font-weight:500}
.prod-name em{display:block;color:var(--muted)}
.prod-name small{display:block;color:var(--green);font-size:9px;margin-top:10px}
/* reviews */
.rev .h{left:150px;width:400px;top:28px}
.review{position:absolute;width:137px;height:90px;border:2px solid var(--card-line);background:var(--white);padding:8px 10px;font-size:5px;line-height:1.45;color:var(--muted)}
.review .who{display:flex;align-items:center;gap:5px;margin-bottom:6px}
.review .av{width:14px;height:14px;border-radius:50%;background:#b9a189}
.review strong{display:block;font-size:6.5px;color:var(--teal)}
.review .stars{color:var(--green);font-size:7px;margin-top:4px;letter-spacing:1px}
.rev .stat-h{position:absolute;left:262px;top:86px;font-size:14px;font-weight:600;color:var(--green)}
.rev ul.list{left:262px;top:128px;width:270px;font-size:13.5px;line-height:1.12}
.rev ul.list li{margin-bottom:6px}
/* action */
.act .photo-act{position:absolute;right:0;top:0;width:330px;height:308px;background:linear-gradient(90deg,var(--teal) 0%,rgba(11,74,79,.55) 45%,rgba(11,74,79,.15) 100%),linear-gradient(160deg,#6f9a6c,#a9c2a0 50%,#587f5a)}
.act .h{left:180px;width:340px;top:26px}
.act .line{position:absolute;left:36px;width:270px;font-size:13px;line-height:1.05;color:var(--white)}
.act .line b{color:var(--green);font-weight:700}
.contact{position:absolute;left:46px;display:flex;align-items:center;gap:10px;font-size:13.5px;color:var(--white)}
.contact svg{width:22px;height:16px}
/* thanks */
.thanks{background:var(--teal-dark)}
.thanks p{position:absolute;left:0;right:0;top:126px;text-align:center;font-size:40px;font-weight:700;color:var(--green)}
</style>
</head>
<body>

<section class="overview" aria-label="Folienübersicht">
  <div class="mini" style="left:30px;top:40px"><div class="slide"><div class="title-word">Lumavita<i></i></div><div class="title-tag">Täglicher Baustein Zukunft</div></div></div>
  <div class="mini" style="left:420px;top:40px"><div class="slide prod"><div class="brand"><i></i>Lumavita</div><div class="h">Ausgewählte Produkte</div>
    <div class="jar-box" style="left:47px"><div class="jar" role="img" aria-label="Produktfoto einer Dose"></div></div>
    <div class="jar-box" style="left:226px"><div class="jar" role="img" aria-label="Produktfoto einer Dose"></div></div>
    <div class="jar-box" style="left:405px"><div class="jar" role="img" aria-label="Produktfoto einer Dose"></div></div></div></div>
  <div class="mini" style="left:810px;top:40px"><div class="slide dark act"><div class="photo-act" role="img" aria-label="Foto eines aktiven älteren Paares im Park"></div><div class="brand"><i></i>Lumavita</div><div class="h">Handeln &amp; Mitmachen</div>
    <div class="line" style="top:95px"><b>Jetzt testen</b>: Ihr biologisches Alter bestimmen</div></div></div>

  <div class="mini" style="left:30px;top:260px"><div class="slide health"><div class="photo-couple" role="img" aria-label="Foto eines lachenden älteren Paares im Grünen"></div><div class="brand"><i></i>Lumavita</div><div class="h">Gesundes Leben &amp; Langlebigkeit</div>
    <ul class="list"><li>Wissenschaftlich fundierte<br>Empfehlungen geben</li><li>Lebensqualität verbessern</li><li>Gesundes Leben verlängern</li></ul></div></div>
  <div class="mini" style="left:420px;top:260px"><div class="slide"><div class="title-word">Lumavita<i></i></div><div class="title-tag">Täglicher Baustein Zukunft</div></div></div>
  <div class="mini" style="left:810px;top:260px"><div class="slide feat"><div class="brand"><i></i>Lumavita</div><div class="h">Hauptmerkmale &amp; Wissenschaftlicher Ansatz</div>
    <div class="pic" style="left:18px;top:82px;background:linear-gradient(160deg,#6c8f5f,#b9cba7)" role="img" aria-label="Foto"></div>
    <div class="pic" style="left:118px;top:100px;background:linear-gradient(160deg,#8f8fa8,#e3d7cf)" role="img" aria-label="Foto"></div>
    <div class="pic" style="left:22px;top:178px;background:linear-gradient(160deg,#b4c0b8,#e8ded6)" role="img" aria-label="Foto"></div>
    <div class="pic" style="left:120px;top:200px;background:linear-gradient(160deg,#d9c8b8,#f2e8e0)" role="img" aria-label="Foto"></div></div></div>

  <div class="mini" style="left:30px;top:480px"><div class="slide dark act"><div class="photo-act" role="img" aria-label="Foto eines aktiven älteren Paares im Park"></div><div class="brand"><i></i>Lumavita</div><div class="h">Handeln &amp; Mitmachen</div>
    <div class="line" style="top:95px"><b>Jetzt testen</b>: Ihr biologisches Alter bestimmen</div></div></div>
  <div class="mini" style="left:420px;top:480px"><div class="slide rev"><div class="brand"><i></i>Lumavita</div><div class="h">Wirkung &amp; Kundenstimmen</div><div class="stat-h">Statistiken:</div>
    <ul class="list"><li>Über 5.000 Kunden</li><li>Bewertung: 4,8/5- 98 % Kundenzufriedenheit</li><li>Reduzierung des biologischen Alters um 5,2 Jahre</li></ul></div></div>
  <div class="mini" style="left:810px;top:480px"><div class="slide"><div class="title-word">Lumavita<i></i></div><div class="title-tag">Täglicher Baustein Zukunft</div></div></div>
</section>

<section class="sheet" aria-label="Folien">
  <div class="slide" style="left:24px;top:60px">
    <div class="title-word" style="top:116px">Lumavita<i></i></div>
    <div class="title-tag" style="top:182px">Täglicher Baustein Zukunft</div>
  </div>

  <div class="slide health" style="left:622px;top:60px">
    <div class="photo-couple" role="img" aria-label="Foto eines lachenden älteren Paares im Grünen"></div>
    <div class="brand"><i></i>Lumavita</div>
    <div class="h">Gesundes Leben &amp;<br>Langlebigkeit</div>
    <div class="sub">Für ein aktives und gesundes Leben – jeden Tag</div>
    <ul class="list"><li>Wissenschaftlich fundierte<br>Empfehlungen geben</li><li>Lebensqualität verbessern</li><li>Gesundes Leben verlängern</li></ul>
  </div>

  <div class="slide feat" style="left:24px;top:438px">
    <div class="brand"><i></i>Lumavita</div>
    <div class="h">Hauptmerkmale &amp;<br>Wissenschaftlicher Ansatz</div>
    <div class="pic" style="left:16px;top:78px;background:linear-gradient(160deg,#6c8f5f,#b9cba7)" role="img" aria-label="Foto eines joggenden älteren Paares"></div>
    <div class="pic" style="left:116px;top:100px;background:linear-gradient(160deg,#8f8fa8,#e3d7cf)" role="img" aria-label="Foto einer Frau im Profil mit DNA-Grafik"></div>
    <div class="pic" style="left:20px;top:176px;background:linear-gradient(160deg,#b4c0b8,#e8ded6)" role="img" aria-label="Foto einer Frau, halb jung, halb älter"></div>
    <div class="pic" style="left:120px;top:200px;background:linear-gradient(160deg,#d9c8b8,#f2e8e0)" role="img" aria-label="Foto einer Frau mit Blume"></div>
    <ul class="list">
      <li><b>Langlebigkeitstest:</b> <em>Bestimmung des biologischen Alters und des Gesundheitspotenzials</em></li>
      <li><b>Analyse &amp; Empfehlungen:</b> <em>Datenverarbeitung für personalisierte Beratung</em></li>
      <li><b>Premium-Produkte:</b> <em>Wissenschaftlich fundierte Formeln für Energie, Gehirn- und Zellgesundheit</em></li>
      <li><b>Fachartikel:</b> <em>NAD+, Epigenetik und Zellernährung</em></li>
    </ul>
  </div>

  <div class="slide prod" style="left:622px;top:438px">
    <div class="brand"><i></i>Lumavita</div>
    <div class="h">Ausgewählte Produkte</div>
    <div class="jar-box" style="left:47px"><div class="jar" role="img" aria-label="Produktfoto der Dose Langlebigkeitskomplex"></div></div>
    <div class="jar-box" style="left:226px"><div class="jar" role="img" aria-label="Produktfoto der Dose Mikronährstoff-Energie"></div></div>
    <div class="jar-box" style="left:405px"><div class="jar" role="img" aria-label="Produktfoto der Dose Kognitives Gehirn"></div></div>
    <div class="prod-name" style="left:18px"><span>Langlebigkeitskomplex</span><em>Unterstützung für ein langes Leben</em><small>€49,90</small></div>
    <div class="prod-name" style="left:197px"><span>Mikronährstoff-Energie</span><em>Energie &amp; Vitalität</em><small>€45,90</small></div>
    <div class="prod-name" style="left:376px"><span>Kognitives Gehirn</span><em>Konzentration &amp; Gehirnfunktion</em><small>€44,90</small></div>
  </div>

  <div class="slide rev" style="left:24px;top:806px">
    <div class="brand"><i></i>Lumavita</div>
    <div class="h">Wirkung &amp; Kundenstimmen</div>
    <div class="review" style="left:30px;top:86px">
      <div class="who"><div class="av"></div><div><strong>Renate Kessler</strong>Lehrerin • 48 Jahre</div></div>
      „Ich fühle mich wacher und ausgeglichener. Die Laborwerte zeigen klare Fortschritte. Das flexible Abo passt perfekt zu mir.“
      <div class="stars">★★★★★</div>
    </div>
    <div class="review" style="left:84px;top:178px">
      <div class="who"><div class="av"></div><div><strong>Jonas Albrecht</strong>Unternehmer • 58 Jahre</div></div>
      „Endlich eine fundierte Lösung für gesundes Altern. Die Empfehlungen sind präzise und die Produkte geben mir Sicherheit.“
      <div class="stars">★★★★★</div>
    </div>
    <div class="stat-h">Statistiken:</div>
    <ul class="list"><li>Über 5.000 Kunden</li><li>Bewertung: 4,8/5- 98 %<br>Kundenzufriedenheit</li><li>Reduzierung des biologischen<br>Alters um 5,2 Jahre</li></ul>
  </div>

  <div class="slide dark act" style="left:627px;top:804px">
    <div class="photo-act" role="img" aria-label="Foto eines aktiven älteren Paares im Park"></div>
    <div class="brand"><i></i>Lumavita</div>
    <div class="h">Handeln &amp; Mitmachen</div>
    <div class="line" style="top:95px"><b>Jetzt testen</b>: Ihr biologisches Alter bestimmen</div>
    <div class="line" style="top:137px"><b>Abonnieren:</b> Erhalten Sie Einblicke in ein langes Leben und exklusive Angebote</div>
    <div class="contact" style="top:206px"><svg viewBox="0 0 22 16" fill="none" stroke="#8cc63f" stroke-width="1.5"><rect x="1" y="1" width="20" height="14"/><path d="M1 1l10 8 10-8M1 15l7-7M21 15l-7-7"/></svg>hallo@lumavita-mail.com</div>
    <div class="contact" style="top:232px"><svg viewBox="0 0 22 16" fill="none" stroke="#8cc63f" stroke-width="1.5"><rect x="2" y="1" width="18" height="11"/><path d="M1 15h20"/><circle cx="11" cy="6.5" r="3"/></svg>www.lumavita-web.com</div>
    <div class="contact" style="top:263px"><svg viewBox="0 0 22 16" fill="#8cc63f"><path d="M2 5c0-3 18-3 18 0v2h-4V5H6v2H2z"/><path d="M5 8h12l2 7H3z"/></svg>+552 000 3197</div>
  </div>

  <div class="slide thanks" style="left:36px;top:1220px">
    <p>Thank you..</p>
  </div>
</section>

<div class="foot"></div>
</body>
</html>
```